VANDIR/ VANDIR GREY Business Card

We have two brands that we would like to show one 1 business card (front and back). We would to incorporate two different logos on one card (VANDIR and VANDIR GREY). Card can be two sided. Simple, sleek and professional.

We are a senior living provider.

www.vandir-example.com
www.vandirgrey-example.com

Target Market(s)

Professionals

Industry/Entity Type

Business

Font styles to use
Serif

Colors

Designer to choose colors to be used in the design.

Requirements
Must have
• Space for EMAIL, PHONE, WEBSITE
Nice to have
• Raised lettering or gloss lettering

```html
<!DOCTYPE html>
<html lang="en">
<head>
<meta charset="utf-8">
<title>Vandir / Vandir Grey Business Card</title>
<link rel="stylesheet" href="https://fonts.googleapis.com/css2?family=Tinos&family=Open+Sans:wght@400&display=swap">
<style>
  :root {
    --paper: #ffffff;
    --frame: #333333;
    --card-light: #4b555b;
    --card-dark: #2a2b2b;
    --gold: #c9a04a;
    --white: #f4f4f4;
  }
  * { margin: 0; padding: 0; box-sizing: border-box; }
  html, body { width: 955px; height: 1200px; overflow: hidden; background: var(--paper); }
  .sheet {
    position: relative;
    width: 955px; height: 1200px;
    border: 1px solid var(--frame);
    background: var(--paper);
  }
  .card {
    position: absolute;
    left: 80px; width: 819px; height: 481px;
    background: radial-gradient(ellipse at 50% 50%, var(--card-light) 0%, #3a4043 45%, var(--card-dark) 100%);
  }
  .card--front { top: 91px; }
  .card--back { top: 620px; }

  .brand {
    position: absolute;
    display: flex; align-items: center;
    font-family: "Tinos", serif;
    color: var(--gold);
    font-weight: 400;
    white-space: nowrap;
  }
  .brand__square { background: var(--gold); flex: none; }

  .front-brand { left: 203px; top: 177px; font-size: 44px; letter-spacing: 1px; }
  .front-brand .brand__square { width: 56px; height: 56px; margin-right: 14px; }

  .tagline {
    position: absolute; left: 273px; top: 229px;
    font-family: "Open Sans", sans-serif;
    font-size: 19.5px; color: var(--white);
  }
  .divider {
    position: absolute; left: 204px; top: 265px;
    width: 411px; height: 2px; background: var(--white);
  }
  .front-web {
    position: absolute; left: 0; right: 0; top: 282px;
    text-align: center;
    font-family: "Tinos", serif; font-size: 24px;
    letter-spacing: 5px; color: var(--gold);
  }

  .back-brand { left: 262px; top: 190px; font-size: 60px; letter-spacing: 1px; }
  .back-brand .brand__square { width: 52px; height: 52px; margin-right: 20px; }

  .contact {
    position: absolute; top: 403px;
    display: flex; align-items: center;
    font-family: "Tinos", serif; color: var(--gold);
  }
  .contact--phone { left: 42px; }
  .contact--email { left: 244px; }
  .contact--web { left: 553px; font-size: 27px; }
  .contact__rule { width: 2px; height: 34px; background: var(--gold); margin-right: 5px; }
  .contact__icon { width: 18px; height: 18px; margin-right: 10px; }
</style>
</head>
<body>
<main class="sheet">

  <section class="card card--front">
    <div class="brand front-brand"><span class="brand__square"></span>VANDIR GREY</div>
    <p class="tagline">Executive Personal Care Services</p>
    <div class="divider"></div>
    <p class="front-web">www.vandirgrey-example.com</p>
  </section>

  <section class="card card--back">
    <div class="brand back-brand"><span class="brand__square"></span>VANDIR</div>

    <div class="contact contact--phone">
      <svg class="contact__icon" viewBox="0 0 18 18" aria-label="Phone">
        <circle cx="9" cy="9" r="9" fill="var(--gold)"/>
        <path d="M6 4.5c.6 0 1.4 1.6 1.4 2.1 0 .5-.8.8-.7 1.2.3 1 1.3 2 2.3 2.3.4.1.7-.7 1.2-.7.5 0 2.1.8 2.1 1.4 0 .9-1 1.7-1.9 1.7C7.4 12.5 5.5 10.6 4.5 7.6c0-.9.6-3.1 1.5-3.1z" fill="#2f3335"/>
      </svg>
    </div>

    <div class="contact contact--email">
      <span class="contact__rule"></span>
      <svg class="contact__icon" viewBox="0 0 18 18" aria-label="Email">
        <rect x="0" y="0" width="18" height="18" rx="2" fill="var(--gold)"/>
        <rect x="3.5" y="5" width="11" height="8" fill="none" stroke="#2f3335" stroke-width="1.4"/>
        <path d="M3.5 5l5.5 4.5 5.5-4.5" fill="none" stroke="#2f3335" stroke-width="1.4"/>
      </svg>
    </div>

    <div class="contact contact--web">
      <span class="contact__rule"></span>
      <svg class="contact__icon" viewBox="0 0 18 18" aria-label="Website">
        <rect x="0" y="0" width="18" height="18" rx="2" fill="var(--gold)"/>
        <circle cx="9" cy="9" r="5.5" fill="none" stroke="#2f3335" stroke-width="1.2"/>
        <ellipse cx="9" cy="9" rx="2.4" ry="5.5" fill="none" stroke="#2f3335" stroke-width="1"/>
        <path d="M3.5 9h11M4.5 6h9M4.5 12h9" stroke="#2f3335" stroke-width="1"/>
      </svg>
      <span>www.vandir-example.com</span>
    </div>
  </section>

</main>
</body>
</html>
```